Insight Plus. needs Business Cards

For this project, we need business cards (currently have also put a call out for a logo). We are a start-up called Insight Plus. This is our second company (our first one was called Querivance). Traditionally we have been providing market research services across different sectors, primarily financial services and the pharmaceutical industry. However, we now want to go beyond market research to offer more (Plus.)... strategic consulting and big data knowledge management. We want our brand to be approachable, creative, fun but professional.

Target Market(s)

The target audience is a business professional - we are B2B (business to business) and do not sell our services to individuals. The brands we work with are major brands across industries, but primarily automotive, financial and pharmaceutical.

Industry/Entity Type

Market Research

Font styles to use
Serif
Sans Serif
Other font styles liked:
• Calibri

Requirements
Must have
• Be clean, simple, modern
Show our address and phone number and email address and website URL
We do not need to have titles showing.

```html
<!DOCTYPE html>
<html lang="en">
<head>
<meta charset="utf-8">
<title>Insight Plus. Business Cards</title>
<link rel="stylesheet" href="https://fonts.googleapis.com/css2?family=Michroma&display=swap">
<style>
  :root {
    --brand-blue: #0b4f9c;
    --brand-red: #cf1331;
    --paper-top: #ffffff;
    --paper-bottom: #e6e6e6;
    --ink-grey: #4a4a4a;
    --stage: #ececec;
    --white: #ffffff;
  }
  * { margin: 0; padding: 0; box-sizing: border-box; }
  html, body { width: 1200px; height: 900px; overflow: hidden; }
  body {
    background: var(--stage);
    font-family: "Michroma", sans-serif;
    display: flex;
    flex-direction: column;
    align-items: center;
    justify-content: center;
    gap: 40px;
  }
  .card {
    position: relative;
    width: 660px;
    height: 377px;
    border-radius: 34px;
    overflow: hidden;
    box-shadow: 0 6px 18px rgba(0,0,0,0.15);
  }
  .card-front {
    background: linear-gradient(160deg, var(--paper-top) 0%, var(--paper-bottom) 100%);
  }
  .front-waves { position: absolute; inset: 0; width: 100%; height: 100%; }
  .brand-name {
    position: absolute;
    left: 40px;
    top: 40px;
    font-size: 36px;
    font-weight: 400;
    color: var(--brand-blue);
    letter-spacing: 0.5px;
  }
  .holder {
    position: absolute;
    left: 30px;
    top: 104px;
    letter-spacing: 2px;
  }
  .holder-name {
    font-size: 15px;
    color: var(--brand-red);
    font-variant: small-caps;
  }
  .holder-role {
    margin-top: 4px;
    font-size: 14px;
    color: var(--ink-grey);
    font-variant: small-caps;
  }
  .contact-list {
    position: absolute;
    left: 400px;
    top: 250px;
    list-style: none;
    color: var(--white);
    font-size: 10.5px;
    letter-spacing: 0.6px;
    line-height: 16px;
  }
  .contact-item { display: flex; align-items: flex-start; gap: 7px; }
  .contact-icon { flex: none; width: 12px; height: 12px; margin-top: 2px; }
  .card-back {
    background: var(--brand-red);
    display: flex;
    align-items: center;
    justify-content: center;
  }
  .brand-name-back {
    font-size: 42px;
    font-weight: 400;
    color: var(--white);
    letter-spacing: 0.5px;
  }
</style>
</head>
<body>

<section class="card card-front">
  <svg class="front-waves" viewBox="0 0 660 377" aria-hidden="true">
    <path d="M0,176 C140,231 260,251 360,244 C470,236 580,166 660,101 L660,377 L0,377 Z" fill="var(--brand-blue)"/>
    <path d="M0,160 C140,215 260,235 360,228 C470,220 580,150 660,85" fill="none" stroke="var(--brand-red)" stroke-width="7"/>
  </svg>

  <div class="brand-name">INSIGHT PLUS.</div>

  <div class="holder">
    <div class="holder-name">Dana Whitfield</div>
    <div class="holder-role">Owner / C.E.O</div>
  </div>

  <ul class="contact-list">
    <li class="contact-item">
      <svg class="contact-icon" viewBox="0 0 12 12"><circle cx="6" cy="6" r="6" fill="#fff"/><path d="M6 2.5a2.2 2.2 0 0 1 2.2 2.2C8.2 6.4 6 9.5 6 9.5S3.8 6.4 3.8 4.7A2.2 2.2 0 0 1 6 2.5z" fill="var(--brand-blue)"/></svg>
      <span>Unit 14, Harbour Court,<br>NY 10418</span>
    </li>
    <li class="contact-item">
      <svg class="contact-icon" viewBox="0 0 12 12"><circle cx="6" cy="6" r="6" fill="#fff"/><path d="M3.6 3c.5-.4 1-.3 1.2.1l.5 1c.2.4 0 .7-.3.9.4.9 1 1.5 1.9 1.9.2-.3.5-.5.9-.3l1 .5c.4.2.5.7.1 1.2-1.6 1.6-6.9-3.7-5.3-5.3z" fill="var(--brand-blue)"/></svg>
      <span>212-555-0148</span>
    </li>
    <li class="contact-item">
      <svg class="contact-icon" viewBox="0 0 12 12"><circle cx="6" cy="6" r="6" fill="#fff"/><rect x="4" y="2.5" width="4" height="7" rx="0.8" fill="var(--brand-blue)"/></svg>
      <span>212-555-0172</span>
    </li>
    <li class="contact-item">
      <svg class="contact-icon" viewBox="0 0 12 12"><circle cx="6" cy="6" r="6" fill="#fff"/><rect x="3" y="4.5" width="6" height="4" rx="0.6" fill="var(--brand-blue)"/><rect x="4" y="2.8" width="4" height="1.7" fill="var(--brand-blue)"/></svg>
      <span>212-555-0193</span>
    </li>
    <li class="contact-item">
      <svg class="contact-icon" viewBox="0 0 12 12"><circle cx="6" cy="6" r="6" fill="#fff"/><rect x="2.8" y="3.8" width="6.4" height="4.4" fill="var(--brand-blue)"/><path d="M2.8 3.8 6 6.4 9.2 3.8" fill="none" stroke="#fff" stroke-width="0.7"/></svg>
      <span>dana@insightplus.example</span>
    </li>
    <li class="contact-item">
      <svg class="contact-icon" viewBox="0 0 12 12"><circle cx="6" cy="6" r="6" fill="#fff"/><circle cx="6" cy="6" r="3.2" fill="none" stroke="var(--brand-blue)" stroke-width="0.9"/><path d="M2.8 6h6.4M6 2.8c-1.4 1.8-1.4 4.6 0 6.4M6 2.8c1.4 1.8 1.4 4.6 0 6.4" fill="none" stroke="var(--brand-blue)" stroke-width="0.7"/></svg>
      <span>www.insightplus.example</span>
    </li>
  </ul>
</section>

<section class="card card-back">
  <div class="brand-name-back">INSIGHT PLUS.</div>
</section>

</body>
</html>
```